"QuobbApps" Website Design

We are a new web/social media development company called "QuobbApps". We need a website homepage and 1 inner page designed. We want visitors to our site to know in the first few seconds that we design and build "apps". We do not want people leaving our homepage not having at least the high level understanding that we design and build "Apps".
We currently have a landing page up at www. quobbapps .com
We specialise in building bespoke
- Vexofon apps
- Drumlet apps
- Pindlerow Apps
- Korvath Apps
- Sunwhistle Apps
- Web applications
- Ulk Apps
- Social Media Marketing Solutions & Strategies
We need a website design concept that is clean, crisp, fresh and says the following about us...
We are a modern web 2.0 company (simple but striking/bold)
We are friendly, professional but dynamic and NOT boring
We are experts in developing apps
We are innovative, modern, energetic and funky
We deliver quality
We can develop to all budgets
The services we offer...
1. App Consultative Services
strategy and planning services for businesses who know they should have an "App" but dont know where to start or what type of App would achieve the best ROI in relation to their objectives.
2. Persona Driven Development leading to Solution & Requirement Design
We help the client understand their audience/target market by developing typical personas of the people who they want to use the app, these personas then drive the solution and the technical requirements. During this process we also pull together written technical specs that outlines the functionality of the app including any mandatory corporate requirements, plus screen-by-screen wireframes of their app with information about page transitions/navigation and any usability requiremens
3. App Design/User Experience Design
We develop a creative look and feel that delivers an outstanding user experience.
We develop Functional Design Specs showing the planned UI (User Interface) design, including the solution design and art direction following client sign off this is passed onto the development team to be programmed along with the apps features.
4. App Development
Turning the idea into a fully functional product with great UI and UX.
5. Maintenance
We offer a range of maintenance packages to suit all budgets, but give our clients piece of mind that there is always someone to call on when problems arise.
Our target audience is
1. anyone with an "App Idea" who needs to get from idea to production
and also
2. small and medium businesses and organisations.
PLEASE NOTE - We do not want a design churned out on an existing website template, so please dont waste your time if this is your normal design process, we will only consider bespoke design concepts that have really considered our brand and needs.
We expect to need additional pages designed which we will obviously look to offer the work to the designer who we choose in this competition.
Attached is a document containing links to websites with a mobile related theme that we like so you can get a feel for our likes and expectations, in addition we have attached our company logo for use in the design.
We dont have any photos or images to use, but are more than happy to pay for stockphotos etc. that are to be used in the final design.
We have not developed the text content or header titles yet so will need placeholder text/headers in place. Once we have the design we have the intention of working the content into the design and making it very search engine friendly, so we are happy for dummy text to be used in the design process unless you feel like making the text relevant.
Updates
Thanks for all the designs so far. General feedback relating to all designs...
Although nice, at present there isnt much "personality" in the designs and in most instances there is too much noise, could you please try and simplify the designs and reduce the amount of things for someone to look at but especially reduce the amount of text read.
3. Increase the amount of space
4. Be bolder with the use of the app brand logos
5. Maybe use more images of different well known smartphone handsets.
6. Vary the size of the typography more
7. Maybe try more vibrant colour combinations, especially with the text
Thanks and good luck
Hi there,
Just to add to the design concept ideas, ive had this image in my mind of the company logo somehow taking centre stage with all things "App" bursting out of it in a fun firework type of way (so smartphones, app brand logos, little square app icons etc.)
Not sure if this is a concept anyone want to attempt to pull something together on but trying to get away from the real "corporate" look. Apps are fun, exciting and interactive, i guess i want the website and the company to get that across about our company, but still get the message across that we are quality driven.
Thanks!
Target Market(s)
and also
Industry/Entity Type
Building
Requirements
Must have
- Clean
Crisp
Not too noisy, with space to breath and read without being overloaded by info.
4 or 5 persistant navigation links (e.g. About, Services, App Platforms, Contact Us, Blog)
The inner page needs to have a subtle contact form - this shouldnt be the focus of the page but just be a feature of it as we intend to have this as a feature on most of the inner pages. The contact form needs space to add info about project, and also a note stating that by submitting their idea we are automatically guaranteeing non disclosure.
Nice to have
- Other things the homepage and maybe the inner pages
A "Join our Pindlerow Fanpage"
A "Follow us on Plimber" link
A space for our plimber/blog/news feed
Should not have
- Should not be based on an off the shelf template layout

```html
<!DOCTYPE html>
<html lang="en">
<head>
<meta charset="utf-8">
<title>QuobbApps – Homepage and About Page</title>
<link rel="stylesheet" href="https://fonts.googleapis.com/css2?family=Arimo:wght@400;700&display=swap">
<style>
  :root {
    --ink: #111111;
    --bar: #0c0c0c;
    --header-grey: #6c6c6a;
    --footer-grey: #9c9c9c;
    --button-grey: #777775;
    --mid-grey: #6f6f6f;
    --lime: #5fc62c;
    --lime-light: #a6db62;
    --lime-pale: #d8f0b0;
    --hero-deep: #79c83a;
    --panel-green: #a2d95c;
    --white: #ffffff;
    --tab-grey: #5b5b5b;
    --font: "Arimo", Arial, sans-serif;
  }
  * { box-sizing: border-box; margin: 0; padding: 0; }
  html, body { width: 1200px; height: 900px; overflow: hidden; background: var(--white); }
  body { font-family: var(--font); color: var(--ink); }
  .canvas { position: relative; width: 1200px; height: 900px; }

  .page { position: absolute; background: var(--white); box-shadow: 3px 4px 6px rgba(0,0,0,.45); overflow: hidden; }
  .page > * { position: absolute; }
  .top-bar { left: 0; right: 0; top: 0; background: var(--bar); }
  .top-nav { position: absolute; color: var(--white); font-weight: 700; white-space: nowrap; }
  .top-pill { position: absolute; background: var(--mid-grey); border-radius: 0 0 0 40px; }
  .site-header { left: 0; right: 0; background: var(--header-grey); }
  .brand-dot { position: absolute; border-radius: 50%; background: var(--lime); }
  .brand-strip { left: 0; right: 0; background: var(--white); z-index: 2; }
  .wordmark { position: absolute; font-weight: 700; color: var(--ink); letter-spacing: -0.5px; white-space: nowrap; }
  .search-field { position: absolute; background: var(--bar); border-radius: 12px 0 0 12px; }
  .search-button { position: absolute; background: var(--lime); border-radius: 0 12px 12px 0; color: var(--ink); display: flex; align-items: center; padding-left: 6px; }
  .hero { left: 0; right: 0; background: linear-gradient(180deg, var(--hero-deep) 0%, var(--lime-light) 55%, var(--lime-pale) 100%); overflow: hidden; }
  .hero > * { position: absolute; }
  .lime-slice { border-radius: 50%; background: radial-gradient(circle at 45% 45%, #e9f8c6 0%, #b6e46e 40%, #7fcb2f 70%, #5aa61f 100%); opacity: .9; }
  .handset {
    border-radius: 30px;
    background:
      radial-gradient(ellipse 38% 30% at 50% 62%, rgba(110,205,60,.9) 0%, rgba(70,150,35,.55) 45%, rgba(0,0,0,0) 100%),
      linear-gradient(160deg, #4a4a4a 0%, #0b0b0b 45%, #1e1e1e 100%);
    box-shadow: inset 0 0 0 4px #9a9a9a, inset 0 0 0 7px #222;
  }
  .side-tab { left: 0; background: var(--tab-grey); border-radius: 0 6px 6px 0; color: var(--white); display: flex; align-items: center; justify-content: center; }
  .side-tab span { writing-mode: vertical-rl; transform: rotate(180deg); letter-spacing: .5px; }
  .side-link { background: var(--white); box-shadow: 1px 1px 3px rgba(0,0,0,.4); color: var(--ink); line-height: 1.15; }
  .site-footer { left: 0; right: 0; background: var(--footer-grey); }
  .footer-row { position: absolute; display: flex; white-space: nowrap; }
  .footer-row dt { font-weight: 700; }
  .page-caption { position: absolute; color: var(--ink); }

  /* homepage */
  .page-home { left: 15px; top: 15px; width: 702px; height: 802px; }
  .page-home .top-bar { height: 18px; }
  .page-home .top-nav { right: 45px; top: 3px; font-size: 10px; }
  .page-home .top-pill { left: 655px; top: 0; width: 47px; height: 18px; }
  .page-home .site-header { top: 18px; height: 107px; }
  .page-home .brand-dot { left: 35px; top: 14px; width: 118px; height: 88px; }
  .page-home .brand-strip { top: 125px; height: 23px; }
  .page-home .wordmark { left: 40px; top: 0; font-size: 21px; line-height: 23px; }
  .page-home .search-field { left: 459px; top: 2px; width: 138px; height: 20px; }
  .page-home .search-button { left: 597px; top: 2px; width: 63px; height: 20px; font-size: 11px; }
  .page-home .hero { top: 148px; height: 269px; }
  .page-home .lime-slice { left: -60px; top: -40px; width: 300px; height: 300px; }
  .welcome { left: 92px; top: 34px; width: 250px; font-size: 41px; line-height: 46px; font-weight: 400; text-align: center; white-space: nowrap; }
  .welcome strong { display: block; font-size: 42px; font-weight: 700; }
  .page-home .handset { left: 368px; top: 30px; width: 250px; height: 260px; }
  .page-home .side-tab { width: 22px; font-size: 10px; }
  .page-home .side-link { left: 22px; font-size: 13px; padding: 6px 4px 0 4px; }

  .features { left: 45px; top: 428px; width: 467px; height: 265px; }
  .feature { position: absolute; top: 0; width: 152px; height: 265px; }
  .feature > * { position: absolute; left: 0; right: 0; }
  .feature-cap { top: 0; height: 20px; background: var(--bar); border-radius: 7px 7px 0 0; }
  .feature-title { top: 22px; height: 45px; font-size: 15px; line-height: 20px; font-weight: 400; text-align: center; white-space: nowrap; }
  .feature-title strong { font-weight: 700; }
  .feature-rule { top: 67px; height: 3px; background: var(--bar); }
  .feature-panel { top: 70px; height: 170px; background: var(--panel-green); border: 2px solid var(--white); }
  .feature-panel p { font-size: 5px; line-height: 6.6px; padding: 4px 6px 0; }
  .feature-panel .sign { padding-top: 1px; }
  .feature-button { left: 7px; right: 7px; top: 194px; height: 43px; background: var(--button-grey); border-radius: 6px; font-size: 11px; line-height: 13px; text-align: center; display: flex; align-items: center; justify-content: center; padding: 0 6px; color: var(--ink); }
  .feature-base { top: 240px; height: 25px; background: var(--bar); border-radius: 0 0 7px 7px; }
  .app-tile {
    position: absolute; left: 18px; top: 10px; width: 112px; height: 108px; border-radius: 6px;
    background:
      radial-gradient(ellipse 45% 38% at 50% 40%, rgba(110,205,60,.95) 0%, rgba(70,150,35,.5) 55%, rgba(0,0,0,0) 100%),
      linear-gradient(160deg, #555, #111);
    display: flex; align-items: flex-end; justify-content: center; padding-bottom: 6px;
    color: #3a3a3a; font-size: 14px;
  }
  .news-column { left: 540px; top: 430px; width: 118px; font-size: 5.2px; line-height: 7.4px; text-align: center; }
  .news-column p + p { margin-top: 7px; }

  .page-home .site-footer { top: 702px; height: 100px; font-size: 5.8px; }
  .page-home .footer-row { left: 34px; }
  .page-home .footer-row dt { width: 67px; }
  .page-home .page-caption { left: 592px; top: 68px; font-size: 18px; }

  /* internal page */
  .page-about { left: 672px; top: 43px; width: 503px; height: 572px; }
  .page-about .top-bar { height: 12px; }
  .page-about .top-nav { right: 32px; top: 2px; font-size: 6.8px; }
  .page-about .top-pill { left: 470px; top: 0; width: 33px; height: 12px; }
  .page-about .site-header { top: 12px; height: 78px; }
  .page-about .brand-dot { left: 25px; top: 5px; width: 86px; height: 68px; }
  .page-about .brand-strip { top: 90px; height: 17px; }
  .page-about .wordmark { left: 28px; top: 0; font-size: 15px; line-height: 17px; }
  .page-about .search-field { left: 328px; top: 1px; width: 98px; height: 15px; }
  .page-about .search-button { left: 426px; top: 1px; width: 64px; height: 15px; font-size: 8px; }
  .page-about .hero { top: 107px; height: 192px; }
  .page-about .lime-slice { left: -40px; top: -30px; width: 200px; height: 200px; }
  .about-title { left: 176px; top: 146px; font-size: 31px; line-height: 36px; font-weight: 400; color: var(--mid-grey); white-space: nowrap; }
  .about-title strong { font-weight: 700; color: var(--ink); }
  .page-about .side-tab { width: 16px; font-size: 8px; }
  .page-about .side-link { left: 16px; font-size: 10px; padding: 4px 3px 0 3px; }
  .page-about .handset { left: 28px; top: 313px; width: 205px; height: 170px; border-radius: 26px; }
  .watch-note { left: 240px; top: 307px; width: 90px; font-size: 12px; line-height: 14px; text-align: center; }
  .watch-arrow { left: 258px; top: 372px; width: 34px; height: 42px; }
  .about-copy { left: 320px; top: 345px; width: 116px; font-size: 3.6px; line-height: 4.6px; }
  .about-copy p + p { margin-top: 5px; }
  .page-about .site-footer { top: 502px; height: 70px; font-size: 4.3px; }
  .page-about .footer-row { left: 24px; }
  .page-about .footer-row dt { width: 49px; }
  .page-about .page-caption { left: 318px; top: 40px; font-size: 18px; }

  .icon-artwork { position: absolute; left: 770px; top: 640px; width: 430px; height: 222px; background: linear-gradient(90deg, #1a1a1a 0%, #3a3a3a 25%, #b9d84a 45%, #2a2a2a 60%, #d7f04c 80%, #1b1b1b 100%); }
  .icon-artwork-reflection { position: absolute; left: 770px; top: 862px; width: 430px; height: 38px; background: linear-gradient(180deg, rgba(120,130,90,.35), rgba(255,255,255,0)); }
</style>
</head>
<body>
<div class="canvas">

  <section class="page page-home" aria-label="QuobbApps homepage">
    <div class="top-bar">
      <nav class="top-nav">Products | My Cart | About Us | Info@</nav>
      <div class="top-pill"></div>
    </div>
    <header class="site-header"><div class="brand-dot"></div></header>
    <div class="brand-strip">
      <div class="wordmark">QuobbApps</div>
      <div class="search-field"></div>
      <div class="search-button">Search</div>
    </div>
    <div class="hero">
      <div class="lime-slice" role="img" aria-label="Photograph of a lime slice"></div>
      <h1 class="welcome">Welcome to <strong>QuobbApps</strong></h1>
      <div class="handset" role="img" aria-label="Photograph of a smartphone showing the QuobbApps app icon"></div>
      <div class="side-tab" style="top:2px;height:42px"></div>
      <div class="side-tab" style="top:47px;height:42px"></div>
      <div class="side-tab" style="top:92px;height:42px"></div>
      <div class="side-tab" style="top:135px;height:42px"><span>APPS</span></div>
      <div class="side-tab" style="top:177px;height:45px"><span>BLOG</span></div>
      <div class="side-tab" style="top:222px;height:45px"><span>INFO@</span></div>
      <a class="side-link" style="top:178px;width:80px;height:42px">Read our Blog here</a>
      <a class="side-link" style="top:223px;width:106px;height:44px">Get in touch with a question</a>
    </div>

    <div class="features">
      <article class="feature" style="left:0">
        <div class="feature-cap"></div>
        <h2 class="feature-title">Testimonials for<br><strong>QuobbApps</strong></h2>
        <div class="feature-rule"></div>
        <div class="feature-panel">
          <p>Lorem ipsum dolor sit amet consectetur adipiscing elit. Vestibulum at est lectus, ut tincidunt lorem integer aliquet. Risus sed convallis suscipit, dui lorem gravida arcu, eget pharetra risus nisl eget mauris. Maecenas congue ipsum at quam pulvinar commodo. Sed vitae nisi lectus, at dictum diam. Suspendisse non mauris sit.</p>
          <p class="sign">Bob, London, UK</p>
          <p>Lorem ipsum dolor sit amet consectetur adipiscing elit. Vestibulum at est lectus, ut tincidunt lorem integer aliquet. Risus sed convallis suscipit, dui lorem gravida arcu, eget pharetra risus nisl eget mauris. Maecenas congue ipsum at quam pulvinar commodo. Sed vitae nisi lectus, at dictum diam. Suspendisse non mauris sit.</p>
          <p class="sign">Sally, California, USA</p>
        </div>
        <a class="feature-button">Click here to see further testimonials for</a>
        <div class="feature-base"></div>
      </article>

      <article class="feature" style="left:157px">
        <div class="feature-cap"></div>
        <h2 class="feature-title">Get free<br><strong>QuobbApp</strong></h2>
        <div class="feature-rule"></div>
        <div class="feature-panel"><div class="app-tile" role="img" aria-label="QuobbApps app icon artwork">QuobbApps</div></div>
        <a class="feature-button">Click here to download our free App</a>
        <div class="feature-base"></div>
      </article>

      <article class="feature" style="left:315px">
        <div class="feature-cap"></div>
        <h2 class="feature-title">Like <strong>QuobbApps</strong> on<br>Pindlerow</h2>
        <div class="feature-rule"></div>
        <div class="feature-panel"><div class="app-tile" role="img" aria-label="QuobbApps app icon artwork for the Pindlerow fan page">Pindlerow</div></div>
        <a class="feature-button">Click here and join us on Pindlerow</a>
        <div class="feature-base"></div>
      </article>
    </div>

    <div class="news-column">
      <p>Lorem ipsum dolor sit amet, consectetur adipiscing elit. Sed imperdiet libero sed nisl laoreet blandit lacus aliquet. Ut placerat nunc lorem, id consectetur purus in nec libero neque. Ut sodales elit ut feugiat lectus tempor. Nullam a sem in erat mattis sagittis sed ac sem. Ut quis est, porttitor quis aliquam in, semper et metus. Aenean ullamcorper, diam sed commodo varius, purus purus viverra quam, at placerat odio lectus ac justo. Fusce non nulla non nisl suscipit hendrerit.</p>
      <p>Lorem ipsum dolor sit amet, consectetur adipiscing elit. Sed imperdiet libero sed nisl laoreet blandit lacus aliquet. Ut placerat nunc lorem, id consectetur purus in nec libero neque. Ut sodales elit ut feugiat lectus tempor. Nullam a sem in erat mattis sagittis sed ac sem. Ut quis est, porttitor quis aliquam in, semper et metus. Aenean ullamcorper, diam sed commodo varius, purus purus viverra quam, at placerat odio lectus ac justo. Fusce non nulla non nisl suscipit hendrerit.</p>
    </div>

    <footer class="site-footer">
      <dl class="footer-row" style="top:8px"><dt>ABOUT QUOBB APPS</dt><dd>HOME PAGE | PINDLEROW PROFILE</dd></dl>
      <dl class="footer-row" style="top:24px"><dt>SERVICES</dt><dd>APP CONSULTATIVE SERVICES | PERSONA DRIVEN DEVELOPMENT | APP DESIGN/ USER EXPERIENCE DESIGN | APP DEVELOPMENT | MAINTENANCE</dd></dl>
      <dl class="footer-row" style="top:40px"><dt>APP PLATFORMS</dt><dd></dd></dl>
      <dl class="footer-row" style="top:56px"><dt>CONTACT</dt><dd>EMAIL | TELEPHONE | TOLVOX</dd></dl>
      <dl class="footer-row" style="top:72px"><dt>BLOG</dt><dd></dd></dl>
      <p class="page-caption">HomePage</p>
    </footer>
  </section>

  <section class="page page-about" aria-label="QuobbApps internal about page">
    <div class="top-bar">
      <nav class="top-nav">Products | My Cart | About Us | Info@</nav>
      <div class="top-pill"></div>
    </div>
    <header class="site-header"><div class="brand-dot"></div></header>
    <div class="brand-strip">
      <div class="wordmark">QuobbApps</div>
      <div class="search-field"></div>
      <div class="search-button">Search</div>
    </div>
    <div class="hero">
      <div class="lime-slice" role="img" aria-label="Photograph of a lime slice"></div>
      <h1 class="about-title">About <strong>QuobbApps</strong></h1>
      <div class="side-tab" style="top:0;height:30px"></div>
      <div class="side-tab" style="top:33px;height:29px"></div>
      <div class="side-tab" style="top:65px;height:30px"></div>
      <div class="side-tab" style="top:95px;height:32px"><span>APPS</span></div>
      <div class="side-tab" style="top:127px;height:31px"><span>BLOG</span></div>
      <div class="side-tab" style="top:158px;height:32px"><span>INFO@</span></div>
      <a class="side-link" style="top:126px;width:57px;height:30px">Read our Blog here</a>
      <a class="side-link" style="top:158px;width:75px;height:32px">Get in touch with a question</a>
    </div>
    <div class="handset" role="img" aria-label="Photograph of a smartphone on its side playing a QuobbApps video"></div>
    <p class="watch-note">Watch this to see what we are all about.</p>
    <svg class="watch-arrow" viewBox="0 0 34 42" aria-hidden="true">
      <path d="M24 2 C26 14 26 26 22 34 C18 38 12 36 8 34" fill="none" stroke="#111" stroke-width="2" stroke-linecap="round"/>
      <path d="M13 27 L7 34 L15 38" fill="none" stroke="#111" stroke-width="2" stroke-linecap="round" stroke-linejoin="round"/>
    </svg>
    <div class="about-copy">
      <p>Lorem ipsum dolor sit amet, consectetur adipiscing elit. Pellentesque ut lorem nunc, vel consequat odio. Vestibulum ante ipsum primis in faucibus orci luctus et ultrices posuere cubilia. Donec vehicula elementum ut commodo nisl. Nulla facilisi. Mauris tincidunt purus nec magna blandit, et egestas ante dignissim. Sed mollis sapien congue.</p>
      <p>Lorem ipsum dolor sit amet, consectetur adipiscing elit. Pellentesque ut lorem nunc, vel consequat odio. Vestibulum ante ipsum primis in faucibus orci luctus et ultrices posuere cubilia. Donec vehicula elementum ut commodo nisl. Nulla facilisi. Mauris tincidunt purus nec magna blandit, et egestas ante dignissim. Sed mollis sapien congue.</p>
    </div>
    <footer class="site-footer">
      <dl class="footer-row" style="top:6px"><dt>ABOUT QUOBB APPS</dt><dd>HOME PAGE | PINDLEROW PROFILE</dd></dl>
      <dl class="footer-row" style="top:18px"><dt>SERVICES</dt><dd>APP CONSULTATIVE SERVICES | PERSONA DRIVEN DEVELOPMENT | APP DESIGN/ USER EXPERIENCE DESIGN | APP DEVELOPMENT | MAINTENANCE</dd></dl>
      <dl class="footer-row" style="top:30px"><dt>APP PLATFORMS</dt><dd></dd></dl>
      <dl class="footer-row" style="top:42px"><dt>CONTACT</dt><dd>EMAIL | TELEPHONE | TOLVOX</dd></dl>
      <dl class="footer-row" style="top:54px"><dt>BLOG</dt><dd></dd></dl>
      <p class="page-caption">Internal About Page</p>
    </footer>
  </section>

  <div class="icon-artwork" role="img" aria-label="Illustrated app icon artwork with black, white and lime paint splatters"></div>
  <div class="icon-artwork-reflection" aria-hidden="true"></div>

</div>
</body>
</html>
```